Higher Resolution Textless Recreation of Existing Album Cover

We're looking to have an old existing album cover of ours recreated at a higher resolution for print.

The original art was created back in 2004 and was only saved at very low resolutions and in odd file formats. It's far too low quality to upscale the original.

The actual art isn't particularly complex. It was made in Photoshop by a non-artist, so we're wanting to see if someone can recreate the art or make something very similar or closely resembles it.

We've uploaded the few versions of the old art that we still have. One is a textless upscale. At the upscale size, the image is way too pixelated (for example, the glowing "tendrils" should be smooth). We included the text version of this as well at its original size. There's also an older version of the cover just to provide as much as we can, but it's a blurrier JPG.

The most important parts to get "right" would be the color tones and the glowing white elements. From what we know, those parts were just generated using the built in Photoshop tools. Since we don't have the original butterflies source layer, we're fine if that can't be matched perfectly.

We'd like it to be 4000x4000 at 300 DPI and textless.

Need extra days to review

```html
<!DOCTYPE html>
<html lang="en">
<head>
<meta charset="utf-8">
<title>Album cover artwork</title>
<style>
  :root {
    --violet-deep: #5e0c92;
    --violet: #8512c4;
    --violet-bright: #a636e0;
    --lilac-glow: #e9c8fb;
    --glow-white: #ffffff;
  }
  html, body {
    margin: 0;
    padding: 0;
    width: 1200px;
    height: 1200px;
    overflow: hidden;
    background: var(--violet);
  }
  .cover {
    position: relative;
    width: 1200px;
    height: 1200px;
    overflow: hidden;
  }
  .cover-art {
    position: absolute;
    inset: 0;
    display: block;
    width: 1200px;
    height: 1200px;
  }
  .field-base { fill: url(#field-gradient); }
  .butterfly-swarm { fill: url(#swarm-gradient); }
  .cloud { fill: var(--glow-white); }
  .cloud-halo { fill: var(--lilac-glow); opacity: 0.55; }
  .tendril { fill: none; stroke: var(--glow-white); stroke-linecap: round; }
  .tendril-halo { fill: none; stroke: var(--lilac-glow); stroke-linecap: round; opacity: 0.6; }
  .sparkle-ray { stroke: var(--glow-white); stroke-width: 1.4; }
</style>
</head>
<body>
  <main class="cover">
    <svg class="cover-art" viewBox="0 0 1200 1200" xmlns="http://www.w3.org/2000/svg">
      <defs>
        <radialGradient id="field-gradient" cx="45%" cy="45%" r="70%">
          <stop offset="0" stop-color="#a83ae2"/>
          <stop offset="0.55" stop-color="#8a16c8"/>
          <stop offset="1" stop-color="#6a0ea4"/>
        </radialGradient>
        <linearGradient id="swarm-gradient" x1="0" y1="0" x2="1" y2="1">
          <stop offset="0" stop-color="#9a1fd8" stop-opacity="0.55"/>
          <stop offset="1" stop-color="#7a10b6" stop-opacity="0.55"/>
        </linearGradient>
        <radialGradient id="sparkle-core">
          <stop offset="0" stop-color="#ffffff"/>
          <stop offset="0.3" stop-color="#ffffff" stop-opacity="0.85"/>
          <stop offset="1" stop-color="#ffffff" stop-opacity="0"/>
        </radialGradient>
        <linearGradient id="ray-h" x1="0" y1="0" x2="1" y2="0">
          <stop offset="0" stop-color="#fff" stop-opacity="0"/>
          <stop offset="0.5" stop-color="#fff"/>
          <stop offset="1" stop-color="#fff" stop-opacity="0"/>
        </linearGradient>
        <linearGradient id="ray-v" x1="0" y1="0" x2="0" y2="1">
          <stop offset="0" stop-color="#fff" stop-opacity="0"/>
          <stop offset="0.5" stop-color="#fff"/>
          <stop offset="1" stop-color="#fff" stop-opacity="0"/>
        </linearGradient>
        <filter id="soft-glow" x="-30%" y="-30%" width="160%" height="160%">
          <feGaussianBlur stdDeviation="9"/>
        </filter>
        <filter id="wide-glow" x="-40%" y="-40%" width="180%" height="180%">
          <feGaussianBlur stdDeviation="26"/>
        </filter>
        <filter id="tendril-glow" x="-20%" y="-20%" width="140%" height="140%">
          <feGaussianBlur stdDeviation="4"/>
        </filter>
        <symbol id="sparkle" viewBox="-90 -90 180 180" overflow="visible">
          <circle r="30" fill="url(#sparkle-core)"/>
          <rect x="-90" y="-0.9" width="180" height="1.8" fill="url(#ray-h)"/>
          <rect x="-0.9" y="-90" width="1.8" height="180" fill="url(#ray-v)"/>
        </symbol>
      </defs>

      <rect class="field-base" width="1200" height="1200"/>

      <!-- Butterfly swarm area -->
      <path class="butterfly-swarm" role="img"
            aria-label="Illustration: rows of violet outlined butterflies drifting diagonally across the cover"
            d="M0 240 L1100 140 L1200 380 L1180 820 L640 900 L80 880 L0 800 Z"
            filter="url(#soft-glow)"/>

      <!-- Soft halos behind the white clouds -->
      <g class="cloud-halos" filter="url(#wide-glow)">
        <ellipse class="cloud-halo" cx="130" cy="140" rx="140" ry="100"/>
        <ellipse class="cloud-halo" cx="1040" cy="440" rx="230" ry="120"/>
        <ellipse class="cloud-halo" cx="1150" cy="120" rx="90" ry="120"/>
        <ellipse class="cloud-halo" cx="60" cy="500" rx="110" ry="130"/>
        <ellipse class="cloud-halo" cx="420" cy="1110" rx="330" ry="120"/>
        <ellipse class="cloud-halo" cx="1100" cy="950" rx="120" ry="60"/>
      </g>

      <!-- Glowing white clouds -->
      <g class="clouds" filter="url(#soft-glow)">
        <ellipse class="cloud" cx="150" cy="150" rx="80" ry="55"/>
        <ellipse class="cloud" cx="60" cy="95" rx="50" ry="35"/>
        <ellipse class="cloud" cx="1175" cy="95" rx="55" ry="70"/>
        <path class="cloud" d="M840 470 C900 420 1000 400 1090 360 C1150 330 1210 320 1210 380 L1210 520 C1140 500 1070 520 1000 540 C930 560 850 540 840 500 Z"/>
        <ellipse class="cloud" cx="1135" cy="270" rx="55" ry="40"/>
        <rect class="cloud" x="890" y="580" width="210" height="54" rx="27" transform="rotate(-28 995 607)"/>
        <path class="cloud" d="M0 430 C60 420 120 440 140 480 C160 540 100 600 40 620 L0 630 Z"/>
        <ellipse class="cloud" cx="175" cy="445" rx="45" ry="22"/>
        <ellipse class="cloud" cx="200" cy="880" rx="40" ry="28"/>
        <ellipse class="cloud" cx="375" cy="885" rx="55" ry="32"/>
        <ellipse class="cloud" cx="1110" cy="930" rx="50" ry="24"/>
        <ellipse class="cloud" cx="1170" cy="565" rx="30" ry="22"/>
        <path class="cloud" d="M1030 770 C1060 740 1120 750 1130 780 C1140 810 1080 830 1050 815 C1025 805 1015 785 1030 770 Z"/>
        <path class="cloud" d="M180 1200 C200 1130 300 1080 400 1070 C500 1060 560 1000 640 990 C720 985 720 1060 680 1120 C650 1170 620 1200 600 1200 Z"/>
        <ellipse class="cloud" cx="470" cy="1000" rx="70" ry="30"/>
      </g>

      <!-- Glowing tendrils -->
      <g class="tendrils">
        <g filter="url(#tendril-glow)">
          <path class="tendril-halo" stroke-width="16" d="M40 1200 C20 1080 90 920 270 770"/>
          <path class="tendril-halo" stroke-width="16" d="M0 1060 C160 1000 360 950 545 920"/>
          <path class="tendril-halo" stroke-width="14" d="M150 1200 C130 1100 170 960 300 830"/>
        </g>
        <path class="tendril" stroke-width="5" d="M40 1200 C20 1080 90 920 270 770"/>
        <path class="tendril" stroke-width="5" d="M0 1060 C160 1000 360 950 545 920"/>
        <path class="tendril" stroke-width="4" d="M150 1200 C130 1100 170 960 300 830"/>
      </g>

      <!-- Star sparkles -->
      <g class="sparkles">
        <use href="#sparkle" x="120" y="-30" width="120" height="120"/>
        <use href="#sparkle" x="505" y="-45" width="120" height="120"/>
        <use href="#sparkle" x="1060" y="-45" width="120" height="120"/>
        <use href="#sparkle" x="745" y="50" width="150" height="150"/>
        <use href="#sparkle" x="390" y="105" width="100" height="100"/>
        <use href="#sparkle" x="75" y="225" width="150" height="150"/>
        <use href="#sparkle" x="525" y="190" width="130" height="130"/>
        <use href="#sparkle" x="300" y="275" width="100" height="100"/>
        <use href="#sparkle" x="670" y="170" width="130" height="130"/>
        <use href="#sparkle" x="915" y="180" width="140" height="140"/>
        <use href="#sparkle" x="780" y="290" width="120" height="120"/>
        <use href="#sparkle" x="395" y="515" width="120" height="120"/>
        <use href="#sparkle" x="630" y="540" width="150" height="150"/>
        <use href="#sparkle" x="15" y="655" width="120" height="120"/>
        <use href="#sparkle" x="-25" y="720" width="100" height="100"/>
        <use href="#sparkle" x="385" y="675" width="130" height="130"/>
        <use href="#sparkle" x="900" y="740" width="140" height="140"/>
        <use href="#sparkle" x="905" y="925" width="160" height="160"/>
        <use href="#sparkle" x="385" y="1075" width="110" height="110"/>
        <use href="#sparkle" x="190" y="1120" width="100" height="100"/>
        <use href="#sparkle" x="180" y="780" width="90" height="90"/>
      </g>
    </svg>
  </main>
</body>
</html>
```